quarry productions business cards design

design a clean look but creative business card for a production company, I'm a freelance producer and launching my startup, would like to keep a clean professional look but still creative

Target Market(s)

businesses

Industry/Entity Type

video production

Contact Information for Business Card

logo, name (Karl Benn), Title (Producer), (MFA Filmmaking, QTSA Los Angeles), contact number & email ID

Colors

Designer to choose only greyscale colors for use in the design.

Requirements
Must have
• logo, black and white colors, you can play with their shades
Nice to have
• a unique design, not necessarily a typical size card
Should not have
• too colorful or playful

```html
<!DOCTYPE html>
<html lang="en">
<head>
<meta charset="utf-8">
<title>Quarry Productions — Business Cards</title>
<link href="https://fonts.googleapis.com/css2?family=Michroma&family=Poppins:wght@400;500&display=swap" rel="stylesheet">
<style>
  :root {
    --bg: #262626;
    --bg-edge: #1c1c1c;
    --card: #161616;
    --card-back-dark: #0b0b0b;
    --card-back-mid: #1f1f1f;
    --white: #f4f4f4;
    --grey: #8e8e8e;
    --rule: #6a6a6a;
  }
  * { margin: 0; padding: 0; box-sizing: border-box; }
  html, body { width: 1200px; height: 1200px; overflow: hidden; }
  body {
    background: radial-gradient(circle at 50% 40%, var(--bg) 0%, var(--bg-edge) 100%);
    position: relative;
    font-family: "Poppins", sans-serif;
  }
  .card {
    position: absolute;
    left: 170px;
    width: 860px;
    height: 491px;
    border-radius: 22px;
    overflow: hidden;
    box-shadow: 0 18px 40px rgba(0,0,0,0.45);
  }
  .card--back { top: 84px; background: var(--card-back-dark); }
  .card--front { top: 625px; background: var(--card); }

  .back-pattern {
    position: absolute; inset: 0;
    background: linear-gradient(90deg, var(--card-back-dark) 0%, var(--card-back-dark) 38%, var(--card-back-mid) 60%, #262626 100%);
  }
  .back-wordmark {
    position: absolute;
    right: 150px; bottom: 82px;
    font-family: "Michroma", sans-serif;
    font-size: 22px;
    letter-spacing: 2px;
    color: var(--white);
  }

  .brand {
    position: absolute;
    left: 70px; top: 190px;
    width: 300px;
    text-align: center;
  }
  .brand__name {
    font-family: "Michroma", sans-serif;
    font-size: 44px;
    color: var(--white);
    line-height: 1.1;
    letter-spacing: 1px;
  }
  .brand__sub {
    font-family: "Michroma", sans-serif;
    font-size: 19.5px;
    color: var(--grey);
    letter-spacing: 2px;
    margin-top: 4px;
  }
  .divider {
    position: absolute;
    left: 400px; top: 130px;
    width: 1px; height: 230px;
    background: var(--rule);
  }
  .person {
    position: absolute;
    left: 445px; top: 140px;
  }
  .person__name {
    font-family: "Michroma", sans-serif;
    font-size: 26px;
    color: var(--white);
    letter-spacing: 1px;
  }
  .person__role {
    font-family: "Michroma", sans-serif;
    font-size: 20px;
    color: var(--grey);
    letter-spacing: 2px;
    margin-top: 2px;
  }
  .contact {
    list-style: none;
    margin-top: 22px;
  }
  .contact__item {
    display: flex;
    align-items: center;
    gap: 14px;
    font-size: 19px;
    color: var(--white);
    letter-spacing: 0.5px;
    height: 38px;
  }
  .contact__icon { width: 30px; height: 22px; flex: none; }
</style>
</head>
<body>

<section class="card card--back" aria-label="Card back">
  <div class="back-pattern" role="img" aria-label="Repeating tonal brand pattern fading from matte black to dark grey"></div>
  <div class="back-wordmark">QUARRY</div>
</section>

<section class="card card--front" aria-label="Card front">
  <div class="brand">
    <div class="brand__name">QUARRY</div>
    <div class="brand__sub">PRODUCTIONS</div>
  </div>

  <div class="divider"></div>

  <div class="person">
    <div class="person__name">KARL BENN</div>
    <div class="person__role">PRODUCER</div>
    <ul class="contact">
      <li class="contact__item">
        <svg class="contact__icon" viewBox="0 0 30 22" fill="none" stroke="#f4f4f4" stroke-width="2.2" stroke-linecap="round">
          <path d="M6 2 Q2 11 6 20"/><path d="M24 2 Q28 11 24 20"/>
          <path d="M11.5 6.5 l2-1.5 1.8 2.8-1.3 1.2 q1 2.3 3 3.4 l1.2-1.2 2.6 1.8-1.4 2 q-5-.6-7.9-8.5z" fill="#f4f4f4" stroke-width="1"/>
        </svg>
        <span>555-014-2280</span>
      </li>
      <li class="contact__item">
        <svg class="contact__icon" viewBox="0 0 30 22" fill="none" stroke="#f4f4f4" stroke-width="2.2" stroke-linecap="round">
          <path d="M6 2 Q2 11 6 20"/><path d="M24 2 Q28 11 24 20"/>
          <rect x="9.5" y="6.5" width="11" height="9" rx="1" stroke-width="1.6"/>
          <path d="M9.5 7 L15 11.5 L20.5 7" stroke-width="1.6"/>
        </svg>
        <span>karl@quarrymail.com</span>
      </li>
      <li class="contact__item">
        <svg class="contact__icon" viewBox="0 0 30 22" fill="none" stroke="#f4f4f4" stroke-width="2.2" stroke-linecap="round">
          <path d="M6 2 Q2 11 6 20"/><path d="M24 2 Q28 11 24 20"/>
          <path d="M15 18 Q10 12.5 10 9.5 a5 5 0 0 1 10 0 Q20 12.5 15 18z" stroke-width="1.6"/>
          <circle cx="15" cy="9.5" r="1.6" stroke-width="1.4"/>
        </svg>
        <span>MFA Filmmaking, QTSA Los Angeles</span>
      </li>
    </ul>
  </div>
</section>

</body>
</html>
```